Need Bold, Hip Card for Concert Ticket Website Gleaming Passes!

Hi there! I am putting together a business/website that sells event tickets (mostly concerts, but also some sports and theater). Think SeatNook, but much smaller. The site is called Gleaming Passes. I have a new logo (attached, with black/red/white color scheme), and am looking for a modern/cool/original business card design. Note that I am thinking of having the card itself in the shape of a ticket (die cut), so you may want to keep that in mind when designing, but I'm not set on that. I'm also open to alternative card sizes, thicknesses, glossy, spot UV, etc. in order to stand out. I'm attaching a potential die cut template and a sample card using that template in case you want to work with that.
Target Market(s)
Music fans, people that like going to see live events
Industry/Entity Type
Entertainment
Contact Information for Business Card
Information that I'd like to have:
website address - www.gleamingpasses.example
phone number: 1-833-5GLEAMNG (532-6264)
my name - Wendel Pike

```html
<!DOCTYPE html>
<html lang="en">
<head>
<meta charset="utf-8">
<title>Gleaming Passes — Business Card</title>
<link rel="stylesheet" href="https://fonts.googleapis.com/css2?family=Montserrat:wght@800&family=Arimo:wght@500&family=Source+Code+Pro:wght@500&display=swap">
<style>
  :root {
    --ink: #080a09;
    --red: #fb0a0f;
    --white: #ffffff;
    --page: #ffffff;
  }
  html, body {
    margin: 0;
    width: 1200px;
    height: 800px;
    overflow: hidden;
    background: var(--page);
  }
  .canvas {
    position: relative;
    width: 1200px;
    height: 800px;
  }
  .card {
    position: absolute;
  }
  .card svg {
    display: block;
  }
  .card-front {
    left: 44px;
    top: 254px;
    width: 512px;
    height: 292px;
  }
  .card-back {
    left: 638px;
    top: 253px;
    width: 514px;
    height: 293px;
  }
  .brand-name {
    position: absolute;
    left: 0;
    right: 0;
    top: 96px;
    margin: 0;
    text-align: center;
    font-family: "Montserrat", sans-serif;
    font-weight: 800;
    font-size: 46px;
    line-height: 48px;
    letter-spacing: 1px;
    color: var(--white);
    text-transform: uppercase;
  }
  .contact {
    position: absolute;
    left: 0;
    right: 0;
    top: 98px;
    text-align: center;
    font-family: "Arimo", sans-serif;
    font-weight: 500;
    font-size: 25px;
    line-height: 25px;
    letter-spacing: -1.3px;
    color: var(--white);
  }
  .contact p {
    margin: 0;
  }
  .website {
    position: absolute;
    left: 0;
    right: 0;
    top: 259px;
    text-align: center;
    font-family: "Source Code Pro", monospace;
    font-weight: 500;
    font-size: 14px;
    letter-spacing: 2.4px;
    color: var(--white);
  }
</style>
</head>
<body>
<main class="canvas">
  <section class="card card-front">
    <svg width="512" height="292" viewBox="0 0 512 292" aria-hidden="true">
      <defs>
        <clipPath id="front-shape">
          <path d="M36 0 H476 A36 36 0 0 0 512 36 V256 A36 36 0 0 0 476 292 H36 A36 36 0 0 0 0 256 V36 A36 36 0 0 0 36 0 Z"/>
        </clipPath>
      </defs>
      <g clip-path="url(#front-shape)">
        <rect width="512" height="292" fill="var(--ink)"/>
        <polygon points="0,314 512,-2 512,300 0,300" fill="var(--red)"/>
      </g>
    </svg>
    <h1 class="brand-name">Gleaming<br>Passes</h1>
  </section>

  <section class="card card-back">
    <svg width="514" height="293" viewBox="0 0 514 293" aria-hidden="true">
      <defs>
        <clipPath id="back-shape">
          <path d="M36 0 H478 A36 36 0 0 0 514 36 V257 A36 36 0 0 0 478 293 H36 A36 36 0 0 0 0 257 V36 A36 36 0 0 0 36 0 Z"/>
        </clipPath>
      </defs>
      <g clip-path="url(#back-shape)">
        <rect width="514" height="293" fill="var(--ink)"/>
        <polygon points="0,2 514,295 514,300 0,300" fill="var(--red)"/>
      </g>
    </svg>
    <div class="contact">
      <p class="contact-name">Wendel Pike</p>
      <p class="contact-phone">1-833-5GLEAMNG (532-6264)</p>
    </div>
    <p class="website">www.gleamingpasses.example</p>
  </section>
</main>
</body>
</html>
```